Sign Design

We already have a logo, but would like to design 2 x signs.
Sign 1:
Dimensions 1500mm wide x 2500m high.
Information to include on sign: - Clinic name and logo (attached)
- the word "DENTIST "
- Street number (which is 348)
Phone number (which is 6153 4097)

Sign 2:
Dimensions: 800mm wide x 600mm high

```html
<!DOCTYPE html>
<html lang="en">
<head>
<meta charset="utf-8">
<title>Kellbrook Dental Care – Sign Designs</title>
<link href="https://fonts.googleapis.com/css2?family=Questrial&family=Arimo:wght@400;700&display=swap" rel="stylesheet">
<style>
  :root {
    --paper: #ffffff;
    --ink: #222222;
    --frame: #333333;
    --green-dark: #1f7a45;
    --green-mid: #4aaa46;
    --green-soft: #a3cc5a;
    --green-pale: #dde9b0;
  }
  html, body {
    margin: 0;
    padding: 0;
    width: 1200px;
    height: 879px;
    overflow: hidden;
    background: var(--paper);
  }
  .canvas {
    position: relative;
    width: 1200px;
    height: 879px;
    font-family: "Arimo", Helvetica, Arial, sans-serif;
    color: var(--ink);
  }
  .sign {
    position: absolute;
    box-sizing: border-box;
    border: 1px solid var(--frame);
    background: var(--paper);
    overflow: hidden;
  }
  .sign--tall { left: 48px; top: 73px; width: 410px; height: 682px; }
  .sign--wide { left: 580px; top: 282px; width: 410px; height: 307px; }

  .dimension-label {
    position: absolute;
    margin: 0;
    font-family: "Questrial", Helvetica, Arial, sans-serif;
    font-size: 21px;
    line-height: 24px;
    color: var(--ink);
    white-space: nowrap;
    transform: translateX(-50%);
  }
  .dimension-label--tall { left: 254px; top: 783px; }
  .dimension-label--wide { left: 786px; top: 236px; }

  .brand-dot {
    position: absolute;
    border-radius: 50%;
    background: var(--green-soft);
  }
  .brand-name {
    position: absolute;
    margin: 0;
    font-family: "Questrial", Helvetica, Arial, sans-serif;
    font-weight: 400;
    color: var(--green-dark);
    line-height: 1;
    letter-spacing: -0.03em;
    white-space: nowrap;
  }
  .brand-name span { display: block; }

  .sign--tall .brand-dot { left: 136px; top: 58px; width: 144px; height: 144px; }
  .sign--tall .brand-name { left: 44px; top: 210px; }
  .sign--tall .brand-main { font-size: 66px; }
  .sign--tall .brand-sub { font-size: 38px; margin: -4px 0 0 114px; }

  .sign--wide .brand-dot { left: 36px; top: 103px; width: 100px; height: 100px; }
  .sign--wide .brand-name { left: 150px; top: 106px; }
  .sign--wide .brand-main { font-size: 50px; }
  .sign--wide .brand-sub { font-size: 28px; margin: -2px 0 0 80px; }

  .sign-headline {
    position: absolute;
    left: 0; right: 0; top: 357px;
    margin: 0;
    text-align: center;
    font-family: "Arimo", Helvetica, Arial, sans-serif;
    font-weight: 700;
    font-size: 66px;
    letter-spacing: 0.06em;
    color: var(--green-dark);
    line-height: 1;
  }
  .footer-band {
    position: absolute;
    left: 0; right: 0; top: 489px; bottom: 0;
    background: linear-gradient(to bottom, var(--green-pale) 0, var(--green-soft) 30px, var(--green-mid) 60px, var(--green-mid) 100%);
  }
  .contact {
    position: absolute;
    left: 0; right: 0; top: 566px;
    margin: 0;
    text-align: center;
    font-size: 38px;
    line-height: 44px;
    color: var(--paper);
  }
  .contact span { display: block; }
</style>
</head>
<body>
<main class="canvas">

  <section class="sign sign--tall" aria-label="Tall street sign">
    <div class="brand-dot" aria-hidden="true"></div>
    <h1 class="brand-name"><span class="brand-main">Kellbrook</span><span class="brand-sub">Dental Care</span></h1>
    <p class="sign-headline">DENTIST</p>
    <div class="footer-band" role="img" aria-label="Decorative green footer band"></div>
    <p class="contact"><span>Street No.348</span><span>Phone 6153 4097</span></p>
  </section>
  <p class="dimension-label dimension-label--tall">Dimensions 1500mm wide x 2500m high</p>

  <p class="dimension-label dimension-label--wide">Dimensions: 800mm wide x 600mm high</p>
  <section class="sign sign--wide" aria-label="Wide wall sign">
    <div class="brand-dot" aria-hidden="true"></div>
    <h2 class="brand-name"><span class="brand-main">Kellbrook</span><span class="brand-sub">Dental Care</span></h2>
  </section>

</main>
</body>
</html>
```